MTSS Pyramid graphic needed for use in presentations and on my website

I am a consultant and need graphics to represent the MTSS pyramid (educational terminology) for use on my website and in slide decks. I've included documentation below that shows the MTSS pyramid, some preferences I have thought of, and my color palette. The MTSS pyramid is well-known in my field and I'd like one that I can use in all my presentations and on my website that looks professional and modern.

Target Market(s)

Educational leaders and educators

Industry/Entity Type

Educational Consulting

Font styles to use
Serif
Sans Serif

Colors
00AB8E
00BBA5
67D7C9
C6EFE9
E9F9F6
6B429C
8869AF
B7A5CE
E3DAEB
F3F0F8

Requirements
Must have
• a pyramid that can be recognized as an MTSS pyramid, use of colors that align with my color palette, a professional, modern look and feel, 3 sections with the largest at the bottom of the pyramid
Nice to have
• rounded corners, maybe 3D
Should not have
• a pyramid in a different shape or orientation, any more or fewer than 3 sections

```html
<!DOCTYPE html>
<html lang="en">
<head>
<meta charset="utf-8">
<title>MTSS Pyramid Set</title>
<link href="https://fonts.googleapis.com/css2?family=Montserrat:wght@500;600;700&display=swap" rel="stylesheet">
<style>
  :root{
    --bg:#ffffff;
    --tier3:#565b7b;
    --tier3-light:#7a7fa3;
    --tier3-dark:#3f4460;
    --tier2:#4f8897;
    --tier2-light:#6fb0bb;
    --tier2-dark:#386d7b;
    --tier1-green:#66b09e;
    --tier1-green-light:#86c9b7;
    --tier1-green-dark:#4c9784;
    --tier1-mint:#a4d8cc;
    --tier1-mint-light:#c3e9df;
    --tier1-mint-dark:#8ccabb;
    --label-light:#ffffff;
    --label-dark:#111418;
  }
  html,body{margin:0;padding:0;overflow:hidden;}
  body{width:1200px;height:3332px;background:var(--bg);position:relative;font-family:"Montserrat",Arial,sans-serif;}
  .pyramid{position:absolute;width:512px;height:428px;}
  .col-left{left:48px;}
  .col-right{left:640px;}
  .row-1{top:300px;}
  .row-2{top:1056px;}
  .row-3{top:1808px;}
  .row-4{top:2556px;}
  .pyramid svg{display:block;width:512px;height:428px;overflow:visible;}
  .tier-tag{font-weight:700;font-size:13px;letter-spacing:.5px;text-anchor:middle;fill:var(--label-light);}
  .tier-name-sm{font-weight:500;font-size:17px;text-anchor:middle;fill:var(--label-light);}
  .tier-name-md{font-weight:500;font-size:31px;text-anchor:middle;fill:var(--label-light);}
  .tier-name-lg{font-weight:600;font-size:42px;text-anchor:middle;fill:var(--label-light);}
  .on-mint .tier1-text{fill:var(--label-dark);}
</style>
</head>
<body>

<svg width="0" height="0" style="position:absolute" aria-hidden="true">
  <defs>
    <clipPath id="pyramid-shape">
      <path d="M236,24 Q256,-6 276,24 L500,392 Q520,428 474,428 L38,428 Q-8,428 12,392 Z"/>
    </clipPath>
    <radialGradient id="g3-tier3" cx="50%" cy="30%" r="75%">
      <stop offset="0" stop-color="var(--tier3-light)"/>
      <stop offset="1" stop-color="var(--tier3-dark)"/>
    </radialGradient>
    <radialGradient id="g3-tier2" cx="50%" cy="35%" r="70%">
      <stop offset="0" stop-color="var(--tier2-light)"/>
      <stop offset="1" stop-color="var(--tier2-dark)"/>
    </radialGradient>
    <radialGradient id="g3-tier1-green" cx="50%" cy="40%" r="70%">
      <stop offset="0" stop-color="var(--tier1-green-light)"/>
      <stop offset="1" stop-color="var(--tier1-green-dark)"/>
    </radialGradient>
    <radialGradient id="g3-tier1-mint" cx="50%" cy="40%" r="70%">
      <stop offset="0" stop-color="var(--tier1-mint-light)"/>
      <stop offset="1" stop-color="var(--tier1-mint-dark)"/>
    </radialGradient>
  </defs>
</svg>

<!-- Rounded 3D, labelled -->
<div class="pyramid col-left row-1">
  <svg viewBox="0 0 512 428">
    <g clip-path="url(#pyramid-shape)">
      <rect x="0" y="270" width="512" height="160" fill="url(#g3-tier1-green)"/>
      <path d="M0,0 H512 V282 Q256,300 0,282 Z" fill="url(#g3-tier2)"/>
      <path d="M0,0 H512 V140 Q256,160 0,140 Z" fill="url(#g3-tier3)"/>
    </g>
    <text class="tier-tag" x="256" y="62">TIER 3</text>
    <text class="tier-name-sm" x="256" y="88">Intensive</text>
    <text class="tier-name-sm" x="256" y="109">Intervention</text>
    <text class="tier-tag" x="256" y="186">TIER 2</text>
    <text class="tier-name-md" x="256" y="220">Targeted</text>
    <text class="tier-name-md" x="256" y="253">Intervention</text>
    <text class="tier-tag" x="256" y="330">TIER 1</text>
    <text class="tier-name-lg tier1-text" x="256" y="374">Core Instruction</text>
  </svg>
</div>

<div class="pyramid col-right row-1 on-mint">
  <svg viewBox="0 0 512 428">
    <g clip-path="url(#pyramid-shape)">
      <rect x="0" y="270" width="512" height="160" fill="url(#g3-tier1-mint)"/>
      <path d="M0,0 H512 V282 Q256,300 0,282 Z" fill="url(#g3-tier2)"/>
      <path d="M0,0 H512 V140 Q256,160 0,140 Z" fill="url(#g3-tier3)"/>
    </g>
    <text class="tier-tag" x="256" y="62">TIER 3</text>
    <text class="tier-name-sm" x="256" y="88">Intensive</text>
    <text class="tier-name-sm" x="256" y="109">Intervention</text>
    <text class="tier-tag" x="256" y="186">TIER 2</text>
    <text class="tier-name-md" x="256" y="220">Targeted</text>
    <text class="tier-name-md" x="256" y="253">Intervention</text>
    <text class="tier-tag tier1-text" x="256" y="330">TIER 1</text>
    <text class="tier-name-lg tier1-text" x="256" y="374">Core Instruction</text>
  </svg>
</div>

<!-- Rounded 3D, blank -->
<div class="pyramid col-left row-2">
  <svg viewBox="0 0 512 428">
    <g clip-path="url(#pyramid-shape)">
      <rect x="0" y="270" width="512" height="160" fill="url(#g3-tier1-green)"/>
      <path d="M0,0 H512 V282 Q256,300 0,282 Z" fill="url(#g3-tier2)"/>
      <path d="M0,0 H512 V140 Q256,160 0,140 Z" fill="url(#g3-tier3)"/>
    </g>
  </svg>
</div>

<div class="pyramid col-right row-2">
  <svg viewBox="0 0 512 428">
    <g clip-path="url(#pyramid-shape)">
      <rect x="0" y="270" width="512" height="160" fill="url(#g3-tier1-mint)"/>
      <path d="M0,0 H512 V282 Q256,300 0,282 Z" fill="url(#g3-tier2)"/>
      <path d="M0,0 H512 V140 Q256,160 0,140 Z" fill="url(#g3-tier3)"/>
    </g>
  </svg>
</div>

<!-- Flat, labelled -->
<div class="pyramid col-left row-3">
  <svg viewBox="0 0 512 428">
    <g clip-path="url(#pyramid-shape)">
      <rect x="0" y="0" width="512" height="142" fill="var(--tier3)"/>
      <rect x="0" y="142" width="512" height="142" fill="var(--tier2)"/>
      <rect x="0" y="284" width="512" height="146" fill="var(--tier1-green)"/>
    </g>
    <text class="tier-tag" x="256" y="62">TIER 3</text>
    <text class="tier-name-sm" x="256" y="88">Intensive</text>
    <text class="tier-name-sm" x="256" y="109">Intervention</text>
    <text class="tier-tag" x="256" y="184">TIER 2</text>
    <text class="tier-name-md" x="256" y="218">Targeted</text>
    <text class="tier-name-md" x="256" y="251">Intervention</text>
    <text class="tier-tag" x="256" y="330">TIER 1</text>
    <text class="tier-name-lg tier1-text" x="256" y="374">Core Instruction</text>
  </svg>
</div>

<div class="pyramid col-right row-3 on-mint">
  <svg viewBox="0 0 512 428">
    <g clip-path="url(#pyramid-shape)">
      <rect x="0" y="0" width="512" height="142" fill="var(--tier3)"/>
      <rect x="0" y="142" width="512" height="142" fill="var(--tier2)"/>
      <rect x="0" y="284" width="512" height="146" fill="var(--tier1-mint)"/>
    </g>
    <text class="tier-tag" x="256" y="62">TIER 3</text>
    <text class="tier-name-sm" x="256" y="88">Intensive</text>
    <text class="tier-name-sm" x="256" y="109">Intervention</text>
    <text class="tier-tag" x="256" y="184">TIER 2</text>
    <text class="tier-name-md" x="256" y="218">Targeted</text>
    <text class="tier-name-md" x="256" y="251">Intervention</text>
    <text class="tier-tag tier1-text" x="256" y="330">TIER 1</text>
    <text class="tier-name-lg tier1-text" x="256" y="374">Core Instruction</text>
  </svg>
</div>

<!-- Flat, blank -->
<div class="pyramid col-left row-4">
  <svg viewBox="0 0 512 428">
    <g clip-path="url(#pyramid-shape)">
      <rect x="0" y="0" width="512" height="142" fill="var(--tier3)"/>
      <rect x="0" y="142" width="512" height="142" fill="var(--tier2)"/>
      <rect x="0" y="284" width="512" height="146" fill="var(--tier1-green)"/>
    </g>
  </svg>
</div>

<div class="pyramid col-right row-4">
  <svg viewBox="0 0 512 428">
    <g clip-path="url(#pyramid-shape)">
      <rect x="0" y="0" width="512" height="142" fill="var(--tier3)"/>
      <rect x="0" y="142" width="512" height="142" fill="var(--tier2)"/>
      <rect x="0" y="284" width="512" height="146" fill="var(--tier1-mint)"/>
    </g>
  </svg>
</div>

</body>
</html>
```